40% Off Colour And Hair Service Every Monday + Wedneday

A large window poster approx 1m x 1m when installed
The poster should in someway match the look of our website
lumerova.net.au
please refer to our website for selection of images and choose something similar yourself
final print needs to suitable for a large format poster

.
.
.
.
.
.
.
.
.
.
.
.
.

Target Market(s)

people passing the salon

Industry/Entity Type

Hair And Beauty

Colors

Designer to choose colors to be used in the design.

Requirements
Must have
• (the offer) : 40% Off Colour And Hair Services Every Monday & Wednesday
• (image) : in keeping with our website : lumerova.net.au
• Phone Number : 9283 5067
• (disclaimer - small print)
• Offer Not Available During Christmas Period. Offer
• Excludes Keratin and Hair Extensions
• 40% discount apples to full price adult services – cannot be combined with any other discount
Nice to have
• in keeping with feel of our website: lumerova.net.au
• must be bold, eye catching and easily readable
• sophisticated / classy / modern feel .. nothing tacky

```html
<!DOCTYPE html>
<html lang="en">
<head>
<meta charset="utf-8">
<title>Lumerova Salon &amp; Spa – 40% Off Colour and Hair Services</title>
<link href="https://fonts.googleapis.com/css2?family=Questrial&family=League+Spartan:wght@600&family=Didact+Gothic&family=Raleway:wght@500&display=swap" rel="stylesheet">
<style>
  :root{
    --paper:#f7f8f9;
    --ink:#0d0d0d;
    --brand-red:#c8102e;
    --divider:#8fd3ea;
    --teal-soft:#7fc9d8;
    --teal-deep:#2f8fa6;
    --hair-dark:#4a160e;
    --hair-mid:#8a3520;
    --hair-light:#b5573a;
    --skin:#d9a387;
  }
  *{margin:0;padding:0;box-sizing:border-box}
  html,body{width:1200px;height:1200px;overflow:hidden;background:var(--paper)}
  .poster{position:relative;width:1200px;height:1200px;background:var(--paper);overflow:hidden;color:var(--ink)}

  .strands-art{
    position:absolute;left:0;top:280px;width:436px;height:820px;
    background:
      radial-gradient(ellipse 70% 45% at 85% 55%, rgba(47,143,166,.45), transparent 70%),
      radial-gradient(ellipse 90% 30% at 20% 20%, rgba(127,201,216,.35), transparent 70%),
      linear-gradient(160deg, rgba(127,201,216,.15), rgba(47,143,166,.3) 60%, rgba(247,248,249,0) 95%);
  }
  .portrait-photo{
    position:absolute;left:436px;top:0;width:764px;height:1200px;
    background:
      radial-gradient(ellipse 38% 40% at 72% 38%, var(--skin), rgba(217,163,135,0) 75%),
      radial-gradient(ellipse 45% 35% at 85% 85%, rgba(204,145,115,.9), rgba(204,145,115,0) 80%),
      linear-gradient(100deg, var(--hair-dark) 0%, var(--hair-mid) 30%, var(--hair-light) 50%, var(--hair-mid) 70%, #f1ece9 100%);
  }
  .divider{position:absolute;left:434px;top:104px;width:2px;height:1096px;background:linear-gradient(var(--paper),var(--divider) 20%,var(--divider))}

  .brand{position:absolute;left:44px;top:64px;width:360px}
  .brand-name{font-family:"League Spartan",sans-serif;font-weight:600;font-size:76px;line-height:1;letter-spacing:-2px;color:var(--brand-red)}
  .brand-tag{margin-top:20px;font-family:"League Spartan",sans-serif;font-weight:600;font-size:24px;letter-spacing:20.5px;white-space:nowrap}

  .offer{position:absolute;left:32px;top:288px;width:380px}
  .offer-amount{font-family:"League Spartan",sans-serif;font-weight:600;font-size:86px;line-height:1;letter-spacing:-1px}
  .offer-line{font-family:"Questrial",sans-serif;font-size:68px;line-height:1;margin-top:6px;letter-spacing:-1px}
  .offer-services{font-family:"League Spartan",sans-serif;font-weight:600;font-size:54px;line-height:1;margin:14px 0 0 6px;letter-spacing:-1px}
  .offer-days{font-family:"Questrial",sans-serif;font-size:50px;line-height:1.12;margin:22px 0 0 6px}

  .terms{position:absolute;left:37px;top:688px;width:300px;font-family:"Didact Gothic",sans-serif;font-size:21px;line-height:27.5px}

  .contact{position:absolute;left:56px;top:1098px;font-family:"Raleway",sans-serif;font-weight:500;font-size:30px}
  .contact-row{display:flex;align-items:center;height:46px}
  .contact-row svg{width:34px;height:34px;margin-right:24px}
</style>
</head>
<body>
<main class="poster">
  <div class="strands-art" role="img" aria-label="Soft blue-teal strands of hair sweeping across from the left"></div>
  <div class="portrait-photo" role="img" aria-label="Portrait of a woman with long glossy auburn-red hair blowing across her face"></div>
  <div class="divider"></div>

  <header class="brand">
    <div class="brand-name">lumerova</div>
    <div class="brand-tag">salon &amp; spa</div>
  </header>

  <section class="offer">
    <div class="offer-amount">40% OFF</div>
    <div class="offer-line">Colour And</div>
    <div class="offer-services">Hair Services</div>
    <div class="offer-days">Every Monday<br>And Wednesday</div>
  </section>

  <p class="terms">*Offer not available<br>during Christmas Period<br>*Offer excludes Keratin<br>and Hair Extensions<br>*40% discount apples to<br>full price adult services –<br>cannot be combined with<br>any other discount</p>

  <footer class="contact">
    <div class="contact-row">
      <svg viewBox="0 0 24 24" fill="none" stroke="#c8102e" stroke-width="1.8"><circle cx="12" cy="12" r="10"/><ellipse cx="12" cy="12" rx="4.5" ry="10"/><line x1="2" y1="12" x2="22" y2="12"/><line x1="4" y1="7" x2="20" y2="7"/><line x1="4" y1="17" x2="20" y2="17"/></svg>
      <span>lumerova.net.au</span>
    </div>
    <div class="contact-row">
      <svg viewBox="0 0 24 24"><path fill="#c8102e" d="M6.6 2.5l3 3.2-1.9 2.6c1.3 2.9 3.3 5 6.1 6.5l2.6-1.9 3.2 3-1.6 3.3c-.4.7-1.2 1-2 .8C9.2 18.3 5.3 14.4 3.5 7.6c-.2-.8.1-1.6.8-2z"/></svg>
      <span>9283 5067</span>
    </div>
  </footer>
</main>
</body>
</html>
```